beauty salon application for consumer

- Find your favorite beauty salons and spas or discover new places next to you with geolocation;
- Filter your search by price, distance, category and type of service;
- Never worry again about having to schedule during your work hours or about not having your calls answered when you want to book an appointment;
- Mark salons as favorites and be the first to be informed of exclusive discounts;
- Don’t ever forget your appointments with Glow Nook’s notifications;
- Compare prices, places and services freely, in a quick and practical way;
- Share reviews about services and places you go with other users and read their opinions;
- USER-FRIENDLY INTERFACE
- GALLERY
- OFFERS

similar interface with application name "primlane"

Industry/Entity Type

Beauty Salon

Font styles to use
Decorative
Script

Colors

Designer to choose colors to be used in the design.

Requirements
Must have
• Please have a look into these applications:
• 1- https://apps.example-store.test/gb/app/primlane/id502918377/?pid=corvella&c=footer-link
• 2- https://apps.example-store.test/us/app/fizz-ltd-book-curl-set-glam-nail-services/id6093817245
• 3- https://market.sample-apps.test/store/apps/details?id=com.lumiparlour.user&hl=en
• 4- https://apps.example-store.test/app/id361720498?mt=8
Nice to have
• Nice to give me a clear screenshots for main function of the application ,please see the above applications before giving me a design .

```html
<!DOCTYPE html>
<html lang="en">
<head>
<meta charset="utf-8">
<title>primlane — Map View</title>
<link rel="stylesheet" href="https://fonts.googleapis.com/css2?family=Roboto:wght@400;500;700&family=Open+Sans:wght@700&display=swap">
<style>
  :root {
    --bg: #ececec;
    --teal: #0b6e98;
    --banner: #434b50;
    --ink: #1c1c1c;
    --map-base: #ecebe8;
    --map-water: #a9d3ee;
    --map-park: #c9e4bf;
    --map-downtown: #f1e9cf;
    --white: #ffffff;
    --star: #f39a1e;
    --star-off: #9a9a9a;
    --user: #1f7cf0;
  }
  * { box-sizing: border-box; margin: 0; padding: 0; }
  html, body { width: 1200px; height: 1200px; overflow: hidden; }
  body {
    background: var(--bg);
    font-family: "Roboto", Arial, sans-serif;
    position: relative;
    color: var(--ink);
  }
  .view-label {
    position: absolute; left: 860px; top: 50px; width: 290px; height: 86px;
    border: 2.5px solid var(--teal); border-radius: 43px;
    display: flex; align-items: center; justify-content: center;
    font-family: "Open Sans", Arial, sans-serif; font-weight: 700;
    font-size: 36px; letter-spacing: 2px; color: var(--teal);
  }
  .screen {
    position: absolute; left: 220px; top: 103px; width: 560px; height: 994px;
    background: var(--white); overflow: hidden; border-radius: 6px;
    box-shadow: 0 10px 40px rgba(0,0,0,.15);
  }
  .status-bar {
    position: absolute; left: 0; top: 0; width: 100%; height: 28px;
    font-size: 17px; display: flex; align-items: center; padding: 0 10px;
    justify-content: space-between;
  }
  .status-bar .carrier, .status-bar .power { display: flex; align-items: center; gap: 5px; }
  .toolbar { position: absolute; top: 28px; left: 0; width: 100%; height: 67px; }
  .menu-icon { position: absolute; left: 15px; top: 20px; }
  .search-icon { position: absolute; left: 506px; top: 18px; }
  .toggle {
    position: absolute; left: 166px; top: 12px; width: 225px; height: 42px;
    border: 2px solid var(--teal); border-radius: 21px; display: flex; overflow: hidden;
    font-weight: 700; font-size: 19px;
  }
  .toggle span { flex: 1; display: flex; align-items: center; justify-content: center; }
  .toggle .active { color: var(--teal); background: var(--white); border-radius: 21px; }
  .toggle .inactive { color: var(--white); background: var(--teal); }
  .results-banner {
    position: absolute; top: 95px; left: 0; width: 100%; height: 36px;
    background: var(--banner); color: var(--white); font-size: 19px; font-weight: 500;
    display: flex; align-items: center; justify-content: center; letter-spacing: .3px;
  }
  .map {
    position: absolute; top: 131px; left: 0; width: 100%; height: 863px;
    background:
      radial-gradient(ellipse 70px 150px at 20px 140px, var(--map-water) 0%, rgba(169,211,238,0) 100%),
      radial-gradient(ellipse 90px 70px at 560px 230px, var(--map-water) 0%, rgba(169,211,238,0) 100%),
      radial-gradient(ellipse 60px 40px at 100px 550px, var(--map-park) 0%, rgba(201,228,191,0) 100%),
      radial-gradient(ellipse 240px 140px at 270px 90px, var(--map-downtown) 0%, rgba(241,233,207,0) 100%),
      linear-gradient(180deg, #e9e7e2 0%, var(--map-base) 50%, #ebebea 100%);
  }
  .map-overlay { position: absolute; left: 0; top: 0; }
  .satellite-thumb {
    position: absolute; left: 30px; top: 885px; width: 80px; height: 80px; border-radius: 50%;
    background: radial-gradient(circle, #7c8f84, #4d6170); border: 3px solid var(--white);
  }
  .filter-fab {
    position: absolute; left: 447px; top: 881px; width: 90px; height: 90px; border-radius: 50%;
    background: var(--teal); display: flex; align-items: center; justify-content: center;
    box-shadow: 0 4px 10px rgba(0,0,0,.25);
  }
  .salon-card {
    position: absolute; left: 95px; top: 373px; width: 370px; height: 231px;
    background: var(--white); border-radius: 10px; box-shadow: 0 3px 12px rgba(0,0,0,.2);
  }
  .salon-card::after {
    content: ""; position: absolute; left: 252px; bottom: -14px;
    border-left: 14px solid transparent; border-right: 14px solid transparent;
    border-top: 14px solid var(--white);
  }
  .salon-photo {
    position: absolute; left: 13px; top: 16px; width: 90px; height: 90px; border-radius: 50%;
    background: radial-gradient(circle at 50% 60%, #8a5a35, #2f2118);
  }
  .salon-name { position: absolute; left: 123px; top: 26px; font-size: 22px; font-weight: 700; white-space: nowrap; }
  .salon-address { position: absolute; left: 123px; top: 61px; font-size: 19px; }
  .salon-rating { position: absolute; left: 123px; top: 89px; display: flex; }
  .salon-meta {
    position: absolute; left: 20px; top: 128px; width: 330px;
    display: flex; justify-content: space-between; font-size: 24px; color: #333;
  }
  .salon-meta div { display: flex; align-items: center; gap: 10px; }
  .book-button {
    position: absolute; left: 13px; top: 171px; width: 343px; height: 45px;
    background: var(--teal); color: var(--white); border-radius: 23px;
    display: flex; align-items: center; justify-content: center;
    font-size: 22px; font-weight: 500; letter-spacing: .5px;
  }
</style>
</head>
<body>
  <div class="view-label">MAP VIEW</div>

  <div class="screen">
    <div class="status-bar">
      <div class="carrier">
        <svg width="22" height="12" viewBox="0 0 22 12"><rect x="0" y="8" width="3" height="4" fill="#222"/><rect x="5" y="6" width="3" height="6" fill="#222"/><rect x="10" y="3" width="3" height="9" fill="#222"/><rect x="15" y="0" width="3" height="12" fill="#222"/></svg>
        <span>Nimbus</span>
        <svg width="18" height="14" viewBox="0 0 18 14"><path d="M1 5a12 12 0 0 1 16 0M4 8a7.5 7.5 0 0 1 10 0M7 11a3 3 0 0 1 4 0" fill="none" stroke="#222" stroke-width="1.8"/></svg>
      </div>
      <span>9:41 AM</span>
      <div class="power">
        <svg width="10" height="16" viewBox="0 0 10 16"><path d="M1 4l8 8-4 3V1l4 3-8 8" fill="none" stroke="#222" stroke-width="1.4"/></svg>
        <span>100%</span>
        <svg width="36" height="16" viewBox="0 0 36 16"><rect x="1" y="1" width="30" height="14" rx="3" fill="none" stroke="#222"/><rect x="3" y="3" width="26" height="10" rx="1.5" fill="#222"/><rect x="32" y="5" width="2.5" height="6" fill="#222"/></svg>
      </div>
    </div>

    <div class="toolbar">
      <svg class="menu-icon" width="30" height="30" viewBox="0 0 30 30" aria-hidden="true">
        <circle cx="7" cy="7" r="6" fill="var(--teal)"/><circle cx="23" cy="7" r="6" fill="var(--teal)"/>
        <circle cx="7" cy="23" r="6" fill="var(--teal)"/><circle cx="23" cy="23" r="6" fill="var(--teal)"/>
      </svg>
      <div class="toggle"><span class="active">MAP</span><span class="inactive">LIST</span></div>
      <svg class="search-icon" width="32" height="32" viewBox="0 0 32 32" aria-hidden="true">
        <circle cx="13" cy="13" r="10" fill="none" stroke="var(--teal)" stroke-width="3.5"/>
        <line x1="20.5" y1="20.5" x2="29" y2="29" stroke="var(--teal)" stroke-width="4" stroke-linecap="round"/>
      </svg>
    </div>

    <div class="results-banner">SHOWING 208 BEAUTY SALONS IN VANCOUVER</div>

    <div class="map" role="img" aria-label="Street map of central Vancouver with downtown, waterfront, neighbourhoods, streets and parks"></div>

    <svg class="map-overlay" width="560" height="994" viewBox="0 0 560 994" aria-hidden="true">
      <defs>
        <g id="pin">
          <line x1="0" y1="0" x2="0" y2="38" stroke="#555" stroke-width="2"/>
          <circle cx="0" cy="0" r="10" fill="var(--teal)"/>
          <circle cx="-3" cy="-3" r="2.5" fill="#fff"/>
        </g>
      </defs>
      <use href="#pin" x="64" y="136"/>
      <use href="#pin" x="256" y="147"/>
      <use href="#pin" x="417" y="164"/>
      <use href="#pin" x="510" y="198"/>
      <use href="#pin" x="195" y="240"/>
      <use href="#pin" x="107" y="285"/>
      <use href="#pin" x="278" y="282"/>
      <use href="#pin" x="328" y="307"/>
      <use href="#pin" x="227" y="355"/>
      <use href="#pin" x="40" y="558"/>
      <use href="#pin" x="132" y="633"/>
      <use href="#pin" x="360" y="639"/>
      <use href="#pin" x="504" y="641"/>
      <use href="#pin" x="372" y="686"/>
      <use href="#pin" x="193" y="714"/>
      <use href="#pin" x="398" y="745"/>
      <use href="#pin" x="547" y="851"/>
      <use href="#pin" x="179" y="868"/>
      <use href="#pin" x="343" y="980"/>
      <circle cx="257" cy="834" r="42" fill="var(--user)" opacity=".15"/>
      <circle cx="257" cy="834" r="12" fill="var(--user)" stroke="#fff" stroke-width="3"/>
    </svg>

    <div class="satellite-thumb" role="img" aria-label="Satellite view toggle thumbnail"></div>

    <div class="filter-fab">
      <svg width="36" height="36" viewBox="0 0 36 36" aria-label="Filter"><path d="M3 5h30L21 19v12l-6-3V19z" fill="#fff"/></svg>
    </div>

    <div class="salon-card">
      <div class="salon-photo" role="img" aria-label="Photo of the salon interior"></div>
      <div class="salon-name">Lumen Salon and Spa</div>
      <div class="salon-address">218 W 9th Ave</div>
      <div class="salon-rating" aria-label="Rated 3 out of 5">
        <svg width="124" height="22" viewBox="0 0 124 22">
          <g fill="none" stroke-width="1.6">
            <circle cx="11" cy="11" r="9.5" stroke="var(--star)"/><circle cx="36" cy="11" r="9.5" stroke="var(--star)"/><circle cx="61" cy="11" r="9.5" stroke="var(--star)"/>
            <circle cx="86" cy="11" r="9.5" stroke="var(--star-off)"/><circle cx="111" cy="11" r="9.5" stroke="var(--star-off)"/>
          </g>
          <g fill="var(--star)">
            <path d="M11 5l1.8 3.8 4 .5-3 2.8.8 4L11 14l-3.6 2.1.8-4-3-2.8 4-.5z"/>
            <path transform="translate(25 0)" d="M11 5l1.8 3.8 4 .5-3 2.8.8 4L11 14l-3.6 2.1.8-4-3-2.8 4-.5z"/>
            <path transform="translate(50 0)" d="M11 5l1.8 3.8 4 .5-3 2.8.8 4L11 14l-3.6 2.1.8-4-3-2.8 4-.5z"/>
          </g>
          <g fill="var(--star-off)">
            <path transform="translate(75 0)" d="M11 5l1.8 3.8 4 .5-3 2.8.8 4L11 14l-3.6 2.1.8-4-3-2.8 4-.5z"/>
            <path transform="translate(100 0)" d="M11 5l1.8 3.8 4 .5-3 2.8.8 4L11 14l-3.6 2.1.8-4-3-2.8 4-.5z"/>
          </g>
        </svg>
      </div>
      <div class="salon-meta">
        <div>
          <svg width="22" height="22" viewBox="0 0 22 22"><circle cx="11" cy="11" r="9" fill="none" stroke="#333" stroke-width="2.2"/><path d="M11 6v5h4" fill="none" stroke="#333" stroke-width="2.2"/></svg>
          <span>12 mins</span>
        </div>
        <div>
          <svg width="18" height="24" viewBox="0 0 18 24"><path d="M9 1a8 8 0 0 1 8 8c0 6-8 14-8 14S1 15 1 9a8 8 0 0 1 8-8z" fill="#333"/><circle cx="9" cy="9" r="3" fill="#fff"/></svg>
          <span>0.7 km</span>
        </div>
      </div>
      <div class="book-button">BOOK NOW</div>
    </div>
  </div>
</body>
</html>
```